Buch-/E-Book-Cover
Zielgruppe
Als Manufaktur einzigartiger Fachmedien präsentiert verlag-kernwerk Schlüsseltechnologien und ihre Märkte. Faszination für Technik ist die Grundlage unserer Arbeit. Mehr als 25 Jahre verlegerische Erfahrung und das Verständnis für Technologiemärkte machen uns zu einem anerkannten Partner der Industrie.
Unsere Medienmarken knüpfen ein starkes und weit verzweigtes Netzwerk – Print und digital – , in dem sich Anbieter und Anwender von Technologien und Produkten in ihren Zielsetzungen wiederfinden.
Unsere Magazine, Events und Netzwerkveranstaltungen sowie kundenspezifische Kommunikations- & Strategiekampagnen setzen in ihren Zielmärkten Maßstäbe und genießen bei Lesern, Kunden und Partnern Vertrauen und Respekt.
Für das ausgeschriebene Projekt handelt es sich um unsere Jahrespublikation MASCHINE.voraus MOLOVETI.
MOLOVETI {polynesisch: Freiraum}
Das Jahrbuch der Industrie. Für Vorwärtsdenker und Zukunftsmacher.
Wandel bestimmt unsere Zeit und verändert unsere Gesellschaft, unsere Unternehmen, uns alle.
Im Wandel liegt Freiraum zur Gestaltung. Gesellschaftlicher Wandel, Technologie-Wandel, Klimawandel, Wertewandel, Führungswandel oder Organisationswandel sind nur einige Beispiele. Wer dabei den Wandel in engen Bahnen denkt, verschenkt Potential. Veränderung braucht Freiraum für neue Ideen und Perspektiven sowie Persönlichkeiten, die diesen nutzen wollen.
Aber wer gestaltet die Zukunft der Industrie und ihrer Branchen? Und wie?
Wir geben 75 Personen aus der Industrie den Freiraum, ihre Perspektiven auf und aus dem Wandel zu erzählen. Warum? Weil sie uns begeistert haben, in persönlichen Treffen und Gesprächen, durch streitbare Meinungen und ehrliche Geschichten. Weil sie die Zukunft verändern.
MOLOVETI ist eine Aufforderung: Zum Mitdenken, Weiterdenken, aber auch Nachdenken.
MOLOVETI – FREIRAUM FÜR IDEEN
Ein Referenzbuch, das den Namen verdient: unkonven..
Aufgabenstellung
1. Kurzzusammenfassung der Ausschreibung
Die 2. Ausgabe des Jahrbuchs der Industrie, MASCHINE.voraus MOLOVETI 2022, erscheint im Oktober 2022. Für das Cover sucht der verlag-kernwerk Verlag neue Vorschläge, die die Themen Freiraum und Wandel in den Fokus stellen und einen optischen Bezug zu der Erstausgabe 2021 setzen.
Die Anforderungen an die Illustration finden Sie untenstehend. Das Marketingteam von verlag-kernwerk wird drei Illustrationen auswählen und im Anschluss die NetzKontor Community von MASCHINE.voraus abstimmen lassen, welches das Sieger-Cover wird. Zusätzlich wird es einen Folgeauftrag für die Gestaltung des Versandkartons geben.
2. Gestalterische & Inhaltliche Anforderungen
• Format: 195x250 mm + Anschnitt
• Rücken: ca. 2 cm (Stand letzte Publikation 2021)
• Auflösung: Druckqualität, mind. 300 dpi
• Inhaltliche Elemente:
- MOLOVETI
- {polynesisch: Freiraum}
- Untersatz: Das Jahrbuch der Industrie. Für Vorwärtsdenker und Zukunftsmacher.
- MASCHINE.voraus Logo
WICHTIG: Entweder soll der aktuelle Schriftzug MOLOVETI oder die Farbe orange (0/80/100/0) (siehe Beispiel MOLOVETI 2021) als Wiedererkennung in die Gestaltungen eingebunden werden.

```html
<!DOCTYPE html>
<html lang="de">
<head>
<meta charset="utf-8">
<title>MOLOVETI 2022 – Jahrbuch der Industrie, Cover und Rücken</title>
<link rel="stylesheet" href="https://fonts.googleapis.com/css2?family=Bebas+Neue&family=Oswald:wght@500;600;700&display=swap">
<style>
  :root {
    --navy: #1f2552;
    --sky-white: #f6fbff;
    --sky-light: #bfe3f7;
    --blue-mid: #4f8fcf;
    --blue-deep: #1d4f9a;
    --blue-dark: #173a78;
    --stage: #ffffff;
    --accent: #d3145a;
  }
  * { margin: 0; padding: 0; box-sizing: border-box; }
  html, body { width: 1200px; height: 720px; overflow: hidden; background: var(--stage); }
  body { position: relative; font-family: "Oswald", "Arial Narrow", sans-serif; color: var(--navy); }

  .spine, .cover { position: absolute; top: 60px; height: 600px; overflow: hidden; box-shadow: 0 2px 6px rgba(0,0,0,.18); }
  .spine { left: 309px; width: 47px; }
  .cover { left: 423px; width: 468px; }

  .backdrop { position: absolute; inset: 0; }
  .cover .backdrop {
    background:
      radial-gradient(ellipse 40% 32% at 32% 24%, var(--sky-white) 0%, rgba(246,251,255,.9) 35%, rgba(191,227,247,.5) 60%, rgba(191,227,247,0) 82%),
      linear-gradient(160deg, var(--sky-light) 0%, var(--blue-mid) 35%, var(--blue-deep) 70%, var(--blue-dark) 100%);
  }
  .spine .backdrop {
    background: linear-gradient(180deg, #d7e6f0 0%, var(--sky-white) 22%, var(--sky-light) 45%, var(--blue-mid) 70%, var(--blue-deep) 100%);
  }

  .title-art { position: absolute; inset: 0; width: 100%; height: 100%; }
  .title-art text { font-family: "Bebas Neue", "Oswald", sans-serif; fill: var(--navy); }
  .cover .title-art text { font-size: 197px; }
  .spine .title-art text { font-size: 38.5px; }

  .translation { position: absolute; left: 306px; top: 296px; font-size: 10.5px; font-weight: 500; white-space: nowrap; }
  .translation em { font-style: italic; }

  .year-vertical { position: absolute; writing-mode: vertical-rl; transform: rotate(180deg); font-weight: 700; line-height: 1; }
  .cover .year-vertical { left: 56px; top: 64px; font-size: 37px; }

  .tagline { position: absolute; left: 58px; top: 146px; font-size: 12.5px; line-height: 14.1px; font-weight: 600; }

  .imprint { position: absolute; left: 58px; top: 336px; display: flex; align-items: center; gap: 3px; font-size: 9px; font-weight: 600; color: var(--navy); }
  .imprint .mark { width: 6px; height: 6px; background: var(--accent); }

  .spine .year-vertical { left: 14px; top: 314px; font-size: 18px; }
  .spine-tagline { position: absolute; left: 18px; top: 354px; writing-mode: vertical-rl; transform: rotate(180deg); font-size: 7.6px; font-weight: 600; line-height: 1; color: var(--navy); white-space: nowrap; }
</style>
</head>
<body>
  <section class="spine" aria-label="Buchrücken">
    <div class="backdrop" role="img" aria-label="Hell-blaue Fotofläche: Blick in eine lichtdurchflutete Glasarchitektur"></div>
    <svg class="title-art" viewBox="0 0 47 600" role="img" aria-label="MOLOVETI">
      <text x="4" y="184">MO</text>
      <text x="4" y="216">LO</text>
      <text x="4" y="248">VE</text>
      <text x="4" y="280">TI</text>
    </svg>
    <p class="year-vertical">2022</p>
    <p class="spine-tagline">Das Jahrbuch der Industrie. Für Vorwärtsdenker und Zukunftsmacher.</p>
  </section>

  <section class="cover" aria-label="Buchcover Vorderseite">
    <div class="backdrop" role="img" aria-label="Fotofläche: Blick nach oben in eine lichtdurchflutete, blaue Glasarchitektur"></div>
    <p class="year-vertical">2022</p>
    <p class="tagline">Das<br>Jahrbuch<br>der<br>Industrie.<br>Für<br>Vorwärts-<br>denker<br>und<br>Zukunfts-<br>macher.</p>
    <div class="imprint"><span class="mark"></span><span>MASCHINE.voraus</span></div>
    <svg class="title-art" viewBox="0 0 468 600" role="img" aria-label="MOLOVETI">
      <text x="260" y="138">MO</text>
      <text x="260" y="289">LO</text>
      <text x="260" y="455">VE</text>
      <text x="260" y="600">TI</text>
    </svg>
    <p class="translation">{<em>polynesisch</em> – Freiraum}</p>
  </section>
</body>
</html>
```